Business Card Design Project

Vexolyte will provide 3D analysis of remote sensing digital data sets of airborne (aircraft/UAV) and satellite data in order to deliver 3D geospatial mapping information, videos and augmented reality products. Typical high end customers are military and security related customers, line object infrastructure owners or providers (pipelines gas/oil/fuel/water, energy lines, borders, coastal zones and rivers, transportation roads on the sea, roads, and railway systems). All these potential customers are linked to regular service monitoring, surveillance and reconnaissance covering cities, counties and countries. The company will provide 3D presentation of infrastructure (which is likely to become a binding requirement in Europe and other countries), disaster prevention and monitoring.

Target Market(s)

Target market are US based governmental agencies, such as Bureau of Civic Safeguards, Federal Terrasight bureau, Ministery of Garrison Affairs, Office of Landholdings/Federal Strata Bureau, etc as well as commercial entities like gas, utilities, etc > Primary services will be to provide 3D geospatial mapping to support search & rescue, border control, infrastructure (pipeline, electric wires, etc.) management, agriculture, climate control, etc.

Industry/Entity Type

Business

Contact Information for Business Card

Vincent Renz6 Gristmill RdCedar Knolls, NJ 079271-973-652-8379vrenz.straight4ward@gmail.com

Requirements
Must have
• Business card must have the company logo (provided) - and want to keep with the colors in the logo

```html
<!DOCTYPE html>
<html lang="en">
<head>
<meta charset="utf-8">
<title>Vexolyte — Business Card</title>
<link rel="stylesheet" href="https://fonts.googleapis.com/css2?family=Source+Sans+3:ital,wght@0,300;0,400;0,600;1,400&display=swap">
<style>
  :root {
    --stage: #3b3b3b;
    --navy: #0f4459;
    --paper: #f6f6f6;
    --signal-red: #d9182d;
    --ink-light: #ffffff;
  }
  * { margin: 0; padding: 0; box-sizing: border-box; }
  html, body {
    width: 1200px; height: 750px; overflow: hidden;
    background: var(--stage);
    font-family: "Source Sans 3", sans-serif;
  }
  .card {
    position: absolute;
    top: 228px;
    width: 461px; height: 262px;
    overflow: hidden;
  }
  .card--front { left: 124px; background: var(--navy); }
  .card--back { left: 618px; background: var(--navy); }

  .front__brand-panel {
    position: absolute; left: 0; top: 0;
    width: 230px; height: 100%;
    background: var(--paper);
  }
  .front__divider {
    position: absolute; left: 230px; top: 0;
    width: 5px; height: 100%;
    background: var(--signal-red);
  }
  .wordmark {
    position: absolute;
    font-weight: 300;
    letter-spacing: 0.5px;
    line-height: 1;
    white-space: nowrap;
    transform: translate(-50%, -50%);
  }
  .front__wordmark { left: 116px; top: 131px; font-size: 36px; color: var(--navy); }

  .contact {
    position: absolute; left: 262px; top: 74px;
    color: var(--ink-light);
  }
  .contact__name { font-size: 18px; font-weight: 600; margin-bottom: 15px; }
  .contact__address { font-size: 11px; line-height: 14px; margin-bottom: 6px; }
  .contact__line {
    display: flex; align-items: center; gap: 6px;
    font-size: 11px; height: 18px;
  }
  .contact__line svg { width: 11px; height: 11px; flex: none; fill: var(--ink-light); }

  .back__wordmark { left: 221px; top: 128px; font-size: 44px; color: var(--ink-light); }
  .back__url {
    position: absolute; left: 0; right: 0; top: 211px;
    text-align: center;
    color: var(--ink-light);
    font-size: 10.5px; font-style: italic;
    letter-spacing: 3px;
  }
</style>
</head>
<body>
  <section class="card card--front">
    <div class="front__brand-panel">
      <span class="wordmark front__wordmark">Vexolyte</span>
    </div>
    <div class="front__divider"></div>
    <div class="contact">
      <p class="contact__name">Harold Brisk</p>
      <p class="contact__address">41 Pelham Ln<br>Maple Hollow, NJ 08314</p>
      <p class="contact__line">
        <svg viewBox="0 0 24 24" aria-hidden="true"><path d="M6.6 10.8a15.1 15.1 0 0 0 6.6 6.6l2.2-2.2a1 1 0 0 1 1-.25 11.4 11.4 0 0 0 3.6.57 1 1 0 0 1 1 1V20a1 1 0 0 1-1 1A17 17 0 0 1 3 4a1 1 0 0 1 1-1h3.5a1 1 0 0 1 1 1c0 1.25.2 2.45.57 3.57a1 1 0 0 1-.25 1z"/></svg>
        555-218-4093
      </p>
      <p class="contact__line">
        <svg viewBox="0 0 24 24" aria-hidden="true"><path d="M12 2a10 10 0 1 0 0 20 10 10 0 0 0 0-20zm6.9 6h-3a15.6 15.6 0 0 0-1.4-3.6A8 8 0 0 1 18.9 8zM12 4a14 14 0 0 1 1.9 4h-3.8A14 14 0 0 1 12 4zM4.3 14a8 8 0 0 1 0-4h3.4a16.5 16.5 0 0 0 0 4zm.8 2h3a15.6 15.6 0 0 0 1.4 3.6A8 8 0 0 1 5.1 16zm3-8h-3a8 8 0 0 1 4.4-3.6A15.6 15.6 0 0 0 8.1 8zM12 20a14 14 0 0 1-1.9-4h3.8A14 14 0 0 1 12 20zm2.3-6H9.7a14.7 14.7 0 0 1 0-4h4.6a14.7 14.7 0 0 1 0 4zm.2 5.6a15.6 15.6 0 0 0 1.4-3.6h3a8 8 0 0 1-4.4 3.6zm1.8-5.6a16.5 16.5 0 0 0 0-4h3.4a8 8 0 0 1 0 4z"/></svg>
        www.vexolyte.example
      </p>
      <p class="contact__line">
        <svg viewBox="0 0 24 24" aria-hidden="true"><path d="M2 5h20v14H2zm2 2v.5l8 5 8-5V7zm0 2.8V17h16V9.8l-8 5z"/></svg>
        hbrisk.onpath22@mailcove.example
      </p>
    </div>
  </section>

  <section class="card card--back">
    <span class="wordmark back__wordmark">Vexolyte</span>
    <p class="back__url">www.vexolyte.example</p>
  </section>
</body>
</html>
```